Poster for Therapy Business

We need an illustrated poster for our massage therapy business.
Looking for a graphic or image that shows we are here to help.
May like some off the wall ideas.

We use a variety of therapies to help people with chronic neck pain, head aches etc.

This poster image needs to be supplied so it wont pixilate in large size but it will also be used for a DL flyer front.

We have logo if needed.

Thanks

Target Market(s)

Target market is people working long hours at computer, admin etc.
People in chronic pain.

Industry/Entity Type

Massage

Requirements
Must have
• Level 1, Brightmark Fitness & Wellbeing,Harlow Business Estate, 417 Feltham Rd,Alexandria, NSW 2015.
www.kvremedial.example.au
(02) 5917 6403
‘help yourself to better health’
Nice to have
• Illustrated graphic
Should not have
• Not interested in the day spa image or typical generic stuff with hands, beautiful women with hots stone etc etc.

```html
<!DOCTYPE html>
<html lang="en">
<head>
<meta charset="utf-8">
<title>Switch On – Massage Therapy Poster</title>
<link href="https://fonts.googleapis.com/css2?family=Roboto+Condensed:wght@300;400&display=swap" rel="stylesheet">
<style>
  :root {
    --paper: #ffffff;
    --ink: #5b6068;
    --ink-soft: #6a6f77;
    --rose-deep: #cf7087;
    --rose-mid: #f0c2cd;
    --rose-pale: #f3e3e5;
    --rose-text: #c8617c;
    --steel-light: #e4e6e8;
    --steel-dark: #9aa0a6;
  }
  * { margin: 0; padding: 0; box-sizing: border-box; }
  html, body {
    width: 927px; height: 1200px; overflow: hidden;
    background: var(--paper);
  }
  .poster {
    position: relative;
    width: 927px; height: 1200px;
    background: var(--paper);
    font-family: "Roboto Condensed", "Helvetica Neue", Arial, sans-serif;
    color: var(--ink);
  }
  .headline {
    position: absolute; left: 0; right: 0; top: 58px;
    text-align: center;
    font-weight: 300; font-size: 72px; letter-spacing: 1px;
    line-height: 1;
  }
  .stripes { position: absolute; left: 0; top: 205px; }
  .switch-art {
    position: absolute; left: 227px; top: 212px;
    width: 470px; height: 417px;
    background: radial-gradient(ellipse at 50% 45%, var(--steel-light) 0%, #c9cdd1 55%, rgba(255,255,255,0) 75%);
  }
  .tagline {
    position: absolute; left: 0; right: 0; top: 682px;
    text-align: center;
    font-weight: 300; font-size: 82px; line-height: 90px;
    letter-spacing: 0.5px;
  }
  .service {
    position: absolute; left: 0; right: 0; top: 906px;
    text-align: center;
    font-weight: 300; font-size: 31px;
    letter-spacing: 15px; color: var(--rose-text);
  }
  .service-motif {
    position: absolute; left: 201px; top: 952px;
    width: 519px; height: 50px; border-radius: 25px;
    background: linear-gradient(90deg, #d98aa0, var(--rose-deep), #d98aa0);
    opacity: 0.8;
  }
  .brand {
    position: absolute; left: 50px; top: 1060px;
    width: 180px; text-align: center;
  }
  .brand-dot {
    width: 56px; height: 56px; border-radius: 50%;
    background: var(--rose-deep); margin: 0 auto 10px;
  }
  .brand-name {
    font-weight: 400; font-size: 17px; line-height: 20px; color: var(--ink);
  }
  .contact {
    position: absolute; left: 250px; top: 1070px;
    color: var(--ink-soft);
  }
  .contact-venue { font-weight: 400; font-size: 29px; line-height: 36px; }
  .contact-line { font-weight: 400; font-size: 17px; line-height: 25px; }
</style>
</head>
<body>
<main class="poster">
  <h1 class="headline">SWITCH ON</h1>

  <svg class="stripes" width="927" height="427" viewBox="0 0 927 427" aria-hidden="true">
    <rect x="23" y="0" width="86" height="427" fill="var(--rose-deep)"/>
    <rect x="133" y="0" width="49" height="427" fill="var(--rose-pale)"/>
    <rect x="201" y="0" width="23" height="427" fill="var(--rose-mid)"/>
    <rect x="701" y="0" width="23" height="427" fill="var(--rose-mid)"/>
    <rect x="742" y="0" width="53" height="427" fill="var(--rose-pale)"/>
    <rect x="817" y="0" width="89" height="427" fill="var(--rose-deep)"/>
  </svg>

  <div class="switch-art" role="img" aria-label="Illustration of a chrome toggle switch flipped to the ON position, with a red ON label above and a black OFF label below"></div>

  <h2 class="tagline">HELP YOURSELF TO<br>BETTER HEALTH</h2>

  <p class="service">massage therapy</p>
  <div class="service-motif" role="img" aria-label="Decorative row of overlapping pink ovals"></div>

  <div class="brand">
    <div class="brand-dot"></div>
    <p class="brand-name">Kestrel Valley Remedial</p>
  </div>

  <address class="contact" style="font-style:normal">
    <p class="contact-venue">Brightmark Fitness &amp; Wellbeing</p>
    <p class="contact-line">Harlow Business Estate, 417 Feltham Rd, Alexandria, NSW 2015</p>
    <p class="contact-line">www.kvremedial.example.au &nbsp;|&nbsp; (02) 5917 6403</p>
  </address>
</main>
</body>
</html>
```